Falcrest security business card

Looking for a business card for my security company

Target Market(s)

Security

Industry/Entity Type

Security

Contact Information for Business Card

Name - Gil Marston. Title - General manager - direct 314 862.4490 website www. falcrestsecurityservices.example email - gil@ falcrestsecurityservices.example

Requirements
Must have
• Logo attached

```html
<!DOCTYPE html>
<html lang="en">
<head>
<meta charset="utf-8">
<title>Falcrest Security Business Card</title>
<link rel="stylesheet" href="https://fonts.googleapis.com/css2?family=Montserrat:wght@500;600&display=swap">
<style>
  :root {
    --stage: #111111;
    --card-top: #1f1f1f;
    --card-bottom: #000000;
    --gold: #b8904a;
    --gold-deep: #a17535;
    --cream: #f6edc0;
    --white: #ffffff;
    --band-dark: #2c2c2c;
    --band-light: #4a4a4a;
  }
  html, body {
    margin: 0;
    width: 1200px;
    height: 1200px;
    overflow: hidden;
    background: var(--stage);
    font-family: "Montserrat", sans-serif;
  }
  .canvas {
    position: relative;
    width: 1200px;
    height: 1200px;
  }
  .card {
    position: absolute;
    left: 226px;
    width: 747px;
    height: 458px;
    overflow: hidden;
    background: linear-gradient(180deg, var(--card-top) 0%, #0c0c0c 55%, var(--card-bottom) 100%);
  }
  .card--front { top: 109px; }
  .card--back { top: 639px; }
  .card__art {
    position: absolute;
    inset: 0;
    width: 747px;
    height: 458px;
  }
  .brand {
    position: absolute;
    transform: translate(-50%, -50%);
    color: var(--gold);
    font-weight: 600;
    font-size: 44px;
    letter-spacing: 1px;
    white-space: nowrap;
  }
  .card--front .brand { left: 570px; top: 97px; }
  .card--back .brand { left: 375px; top: 228px; }
  .holder__name {
    position: absolute;
    left: 38px;
    top: 66px;
    margin: 0;
    color: var(--gold);
    font-weight: 600;
    font-size: 31px;
    letter-spacing: 0.5px;
  }
  .holder__title {
    position: absolute;
    left: 40px;
    top: 110px;
    margin: 0;
    color: var(--white);
    font-weight: 500;
    font-size: 18px;
  }
  .contact {
    position: absolute;
    left: 38px;
    top: 312px;
    margin: 0;
    padding: 0;
    list-style: none;
  }
  .contact__item {
    display: flex;
    align-items: center;
    height: 32.5px;
    color: var(--white);
    font-weight: 500;
    font-size: 19px;
  }
  .contact__icon {
    width: 22px;
    height: 22px;
    margin-right: 20px;
    fill: var(--white);
  }
</style>
</head>
<body>
<main class="canvas">

  <section class="card card--front">
    <svg class="card__art" viewBox="0 0 747 458" aria-hidden="true">
      <defs>
        <linearGradient id="bottomBar" x1="0" x2="1" y1="0" y2="0">
          <stop offset="0" stop-color="#a17535"/>
          <stop offset="0.55" stop-color="#e9d79a"/>
          <stop offset="1" stop-color="#fbf5d2"/>
        </linearGradient>
        <linearGradient id="bandFront" x1="1" y1="0" x2="0" y2="1">
          <stop offset="0" stop-color="#3a3a3a"/>
          <stop offset="1" stop-color="#262626"/>
        </linearGradient>
      </defs>
      <polygon points="747,62 747,92 620,320 606,306" fill="#1a1a1a"/>
      <polygon points="747,130 563,458 747,458" fill="url(#bandFront)"/>
      <polygon points="747,315 662,458 708,458 747,392" fill="var(--band-light)"/>
      <polygon points="624,263 636,263 514,458 502,458" fill="var(--gold-deep)"/>
      <polygon points="0,444 334,444 348,458 0,458" fill="url(#bottomBar)"/>
    </svg>

    <div class="brand">FALCREST</div>

    <h1 class="holder__name">GIL MARSTON</h1>
    <p class="holder__title">General Manager</p>

    <ul class="contact">
      <li class="contact__item">
        <svg class="contact__icon" viewBox="0 0 24 24"><path d="M6.6 10.8a15.1 15.1 0 0 0 6.6 6.6l2.2-2.2a1 1 0 0 1 1-.25 11.4 11.4 0 0 0 3.6.57 1 1 0 0 1 1 1V20a1 1 0 0 1-1 1A17 17 0 0 1 3 4a1 1 0 0 1 1-1h3.5a1 1 0 0 1 1 1c0 1.25.2 2.45.57 3.57a1 1 0 0 1-.25 1z"/></svg>
        314 862.4490
      </li>
      <li class="contact__item">
        <svg class="contact__icon" viewBox="0 0 24 24"><path d="M2 5h20v2.2l-10 6-10-6z"/><path d="M2 9.5l10 6 10-6V19H2z"/></svg>
        gil@ falcrestsecurityservices.example
      </li>
      <li class="contact__item">
        <svg class="contact__icon" viewBox="0 0 24 24"><path d="M3 3l18 8-8 2-2 8z"/></svg>
        www. falcrestsecurityservices.example
      </li>
    </ul>
  </section>

  <section class="card card--back">
    <svg class="card__art" viewBox="0 0 747 458" aria-hidden="true">
      <defs>
        <linearGradient id="bandBack" x1="0" y1="0" x2="1" y2="1">
          <stop offset="0" stop-color="#3a3a3a"/>
          <stop offset="1" stop-color="#262626"/>
        </linearGradient>
      </defs>
      <polygon points="0,9 219,458 0,458" fill="url(#bandBack)"/>
      <polygon points="0,130 108,458 62,458 0,270" fill="var(--band-light)"/>
      <polygon points="152,263 164,263 287,458 275,458" fill="var(--gold-deep)"/>
    </svg>

    <div class="brand">FALCREST</div>
  </section>

</main>
</body>
</html>
```